Nebelkreis - needs a CD/Cover Design for a VA Compilation

We need a CD-Design/Cover-Artwork for our Various Artists Compilation called 'Nebelkreis', which means "Fog circle". Back then our events were based in one of Germanys best underground techno-clubs., which we also called "our temple".
The artists featured on this compilation rather performed at our events or had a massive influence on the music the djs played.
The sound is glitchy, technically detailed and a little unpredictable.

We would like to see some designs not too colourful!

Target Market(s)

complex electronic music listeners

Industry/Entity Type

Club

Font styles to use
Sans Serif

Colors
ec1f27

Requirements
Must have
• Ideally the artwork should be something otherworldly, abstract/glitchy, be an optical illusion and/or have geometric complexity.
Nice to have
• - probably black and white design fits better with us, but you can also try it with a very few colors.
- maybe something futuristic or scatchy
Should not have
• - it should definitely NOT be too colourful.
- no humans!! or animals
- in case you think to draw a temple, please use it more abstract, nothing too obviously, we dont wanna look like a hippie event!
- no musical notes
- no obvious "play" symbol / headphones or vinyl images

```html
<!DOCTYPE html>
<html lang="en">
<head>
<meta charset="utf-8">
<title>Nebelkreis – Various Artists Compilation – CD Cover</title>
<link href="https://fonts.googleapis.com/css2?family=Josefin+Sans:wght@300;400&family=Questrial&display=swap" rel="stylesheet">
<style>
  :root {
    --ink: #000000;
    --signal-red: #ec1f27;
    --smoke-red: #c41a1f;
    --guide: #5fd3d6;
    --edge: #3a3a3a;
  }
  * { margin: 0; padding: 0; box-sizing: border-box; }
  html, body { width: 1200px; height: 549px; overflow: hidden; background: var(--ink); }
  .cover-spread { position: relative; width: 1200px; height: 549px; background: var(--ink); overflow: hidden; }

  .panel { position: absolute; top: 0; height: 549px; overflow: hidden; }
  .panel--back { left: 0; width: 619px; }
  .panel--spine { left: 619px; width: 42px; }
  .panel--front { left: 661px; width: 539px; }

  .smoke-art { position: absolute; inset: 0; }
  .smoke-art--back {
    background:
      radial-gradient(ellipse 190px 70px at 260px 60px, rgba(196,26,31,.85), transparent 70%),
      radial-gradient(ellipse 60px 140px at 20px 190px, rgba(196,26,31,.6), transparent 70%),
      radial-gradient(ellipse 200px 80px at 470px 470px, rgba(196,26,31,.8), transparent 70%),
      radial-gradient(ellipse 120px 50px at 350px 520px, rgba(196,26,31,.5), transparent 70%),
      var(--ink);
  }
  .smoke-art--spine {
    background:
      radial-gradient(ellipse 40px 60px at 20px 200px, rgba(196,26,31,.75), transparent 70%),
      radial-gradient(ellipse 30px 40px at 10px 110px, rgba(196,26,31,.5), transparent 70%),
      var(--ink);
  }
  .smoke-art--front {
    background:
      radial-gradient(ellipse 190px 110px at 130px 120px, rgba(196,26,31,.8), transparent 70%),
      radial-gradient(ellipse 110px 60px at 90px 30px, rgba(196,26,31,.55), transparent 70%),
      radial-gradient(ellipse 260px 110px at 330px 440px, rgba(196,26,31,.85), transparent 70%),
      radial-gradient(ellipse 90px 60px at 510px 240px, rgba(196,26,31,.45), transparent 70%),
      var(--ink);
  }

  .tracklist {
    position: absolute; left: 160px; top: 130px; list-style: none;
    font-family: "Questrial", "Century Gothic", sans-serif;
    font-size: 16px; line-height: 37px; color: var(--signal-red);
  }

  .spine-title {
    position: absolute; left: 21px; top: 224px;
    transform-origin: 0 0; transform: rotate(90deg) translateY(-50%);
    font-family: "Josefin Sans", sans-serif; font-weight: 300;
    font-size: 15px; letter-spacing: 3px; color: var(--signal-red); white-space: nowrap;
  }

  .front-title {
    position: absolute; right: 52px; top: 114px;
    font-family: "Josefin Sans", sans-serif; font-weight: 300;
    font-size: 31px; letter-spacing: 5px; color: var(--signal-red); line-height: 1;
    margin-right: -5px;
  }
  .front-subtitle {
    position: absolute; right: 52px; top: 160px; text-align: right;
    font-family: "Josefin Sans", sans-serif; font-weight: 300;
    font-size: 16px; line-height: 20px; letter-spacing: .5px; color: var(--signal-red);
  }

  .guides { position: absolute; inset: 0; pointer-events: none; }
  .guides line { stroke: var(--guide); stroke-width: 1; }
  .guides .edge { stroke: var(--edge); stroke-width: 2; }
</style>
</head>
<body>
<main class="cover-spread">
  <section class="panel panel--back">
    <div class="smoke-art smoke-art--back" role="img" aria-label="Abstract red smoke-like brush strokes on black"></div>
    <ol class="tracklist">
      <li>Integer aliquet dolor at vehicula</li>
      <li>Mauris et lacus tincidunt</li>
      <li>Etiam pharetra felis vel elit</li>
      <li>Aenean id lacus vitae lorem</li>
      <li>Suspendisse vel velit condimentum</li>
      <li>Cras fermentum urna vel ipsum l</li>
      <li>Integer nec augue eu dui tincidunt</li>
      <li>Etiam nec est at elit maximus malesuada</li>
    </ol>
  </section>

  <section class="panel panel--spine">
    <div class="smoke-art smoke-art--spine" role="img" aria-label="Abstract red smoke strokes continuing across the spine"></div>
    <p class="spine-title">NEBELKREIS</p>
  </section>

  <section class="panel panel--front">
    <div class="smoke-art smoke-art--front" role="img" aria-label="Abstract red smoke-like geometric brush strokes on black"></div>
    <h1 class="front-title">NEBELKREIS</h1>
    <p class="front-subtitle">VARIOUS ARTISTS<br>COMPILATION</p>
  </section>

  <svg class="guides" width="1200" height="549" viewBox="0 0 1200 549" aria-hidden="true">
    <line class="edge" x1="0" y1="1" x2="1200" y2="1"/>
    <line x1="0" y1="14.5" x2="1200" y2="14.5"/>
    <line x1="0" y1="19.5" x2="1200" y2="19.5"/>
    <line x1="0" y1="534.5" x2="1200" y2="534.5"/>
    <line x1="0" y1="539.5" x2="1200" y2="539.5"/>
    <line x1="2.5" y1="0" x2="2.5" y2="549"/>
    <line x1="15.5" y1="0" x2="15.5" y2="549"/>
    <line x1="619.5" y1="0" x2="619.5" y2="549"/>
    <line x1="661.5" y1="0" x2="661.5" y2="549"/>
    <line x1="1185.5" y1="0" x2="1185.5" y2="549"/>
    <line x1="1197.5" y1="0" x2="1197.5" y2="549"/>
  </svg>
</main>
</body>
</html>
```